Fitness Coach Needs Book Cover Created

I would like a book cover created for my upcoming project titled,
Golden Stride After 40: 7 Quiet Rules to Reshape Every Day

Target Market(s)

Men & Women 30-40 years old

Industry/Entity Type

Fitness

Font styles to use
Serif

Requirements
Must have
• 3 color cover. I have attached my name to be used at bottom of cover and uploaded a couple sample covers as well.
Should not have
• stock imaging.

```html
<!DOCTYPE html>
<html lang="en">
<head>
<meta charset="utf-8">
<title>Golden Stride After 40 — Book Cover</title>
<link rel="stylesheet" href="https://fonts.googleapis.com/css2?family=Oswald:wght@400;700&family=Roboto+Condensed:wght@400&display=swap">
<style>
  :root {
    --paper-light: #fbfbfb;
    --paper-edge: #d9d9d9;
    --ink: #141414;
    --ink-soft: #262626;
    --red-bright: #d01f1f;
    --red-deep: #7e0808;
    --tear-white: #f3f1ee;
    --author-grey: #3b3b3b;
  }
  * { margin: 0; padding: 0; box-sizing: border-box; }
  html, body { width: 745px; height: 1200px; overflow: hidden; }
  body { background: var(--paper-edge); }

  .cover {
    position: relative;
    width: 745px;
    height: 1200px;
    overflow: hidden;
    background: radial-gradient(ellipse 75% 60% at 50% 40%, var(--paper-light) 0%, #f0f0f0 55%, var(--paper-edge) 100%);
  }

  .title {
    position: absolute;
    top: 150px;
    left: 0;
    width: 100%;
    text-align: center;
    font-family: "Oswald", sans-serif;
    color: var(--ink);
    text-transform: uppercase;
  }
  .title__main {
    display: block;
    font-weight: 700;
    font-size: 142px;
    line-height: 0.86;
    letter-spacing: -1px;
  }
  .title__tail {
    display: block;
    margin-top: 14px;
    font-weight: 400;
    font-size: 68px;
    line-height: 1;
    letter-spacing: 1px;
    color: var(--ink-soft);
  }

  .band {
    position: absolute;
    top: 630px;
    left: 0;
    width: 745px;
    height: 320px;
  }
  .band__shape { position: absolute; inset: 0; width: 100%; height: 100%; }
  .band__subtitle {
    position: absolute;
    top: 92px;
    left: 0;
    width: 100%;
    text-align: center;
    font-family: "Roboto Condensed", sans-serif;
    font-weight: 400;
    font-size: 46px;
    line-height: 1.32;
    color: #ffffff;
  }

  .author {
    position: absolute;
    top: 975px;
    left: 0;
    width: 100%;
    text-align: center;
    font-family: "Oswald", sans-serif;
    font-weight: 700;
    font-size: 50px;
    letter-spacing: 1px;
    text-transform: uppercase;
    line-height: 1;
  }
  .author__first { color: var(--red-bright); }
  .author__last { color: var(--author-grey); }
</style>
</head>
<body>
  <main class="cover">
    <h1 class="title">
      <span class="title__main">Golden</span>
      <span class="title__main">Stride</span>
      <span class="title__tail">After 40</span>
    </h1>

    <section class="band">
      <svg class="band__shape" viewBox="0 0 745 320" preserveAspectRatio="none" aria-hidden="true">
        <defs>
          <radialGradient id="bandRed" cx="50%" cy="50%" r="65%">
            <stop offset="0%" stop-color="var(--red-bright)"/>
            <stop offset="60%" stop-color="#b01414"/>
            <stop offset="100%" stop-color="var(--red-deep)"/>
          </radialGradient>
        </defs>
        <polygon fill="var(--tear-white)" points="0,14 40,8 85,18 120,6 170,16 215,9 260,20 300,7 345,15 390,5 430,17 480,8 520,18 565,6 610,15 650,9 700,19 745,10 745,312 700,304 655,316 610,302 560,314 515,300 470,311 420,301 375,313 330,303 285,315 240,300 190,312 145,302 100,315 55,303 0,313"/>
        <polygon fill="url(#bandRed)" points="0,24 30,18 70,28 110,16 150,27 200,18 240,29 290,15 335,26 380,17 425,28 470,16 515,27 560,17 600,26 645,15 690,27 745,19 745,298 705,292 660,303 615,290 570,301 520,288 475,299 430,289 380,300 335,290 290,302 245,288 200,299 150,290 105,301 60,291 20,300 0,294"/>
      </svg>
      <p class="band__subtitle">7 Quiet Rules to Reshape<br>Every Day</p>
    </section>

    <p class="author"><span class="author__first">Ray</span><span class="author__last">Montano</span></p>
  </main>
</body>
</html>
```